Dental Health Door hanger for contest to attract new patients

We are a group dental practice located in Burlington, Ontario, Canada. We are looking to bring in new patients and are targeting a new subdivision as well as established neighbourhoods around it.

The door hanger we require is for a contest are offering that will run for approx. 6 months to win a $1000.00 travel gift card. The individual must come in person to drop off the ballot and during that time they will get a tour of the practice and meet key people. There is no requirement for them to make an appointment but that is the ultimate goal.

I have included:
- a picture we typically use, however it is not required (female smiling)
- Our logo with "your city your dentists" below it. We want that tagline removed
- our other logo
- the excel version of the map created to our location
- the current one attempted on our own and is missing something - like the concept but not the total look/ feel

The final design should make the person want to come in and book an appointment with us and at the very least call to schedule something with a dentist.

Target Market(s)

New subdivision and surrounding area for new patients

Industry/Entity Type

Dental Clinic

Colors

Designer to choose colors to be used in the design.

Requirements
Must have
• Our address is 1846 Pinecrest Road, Burlington, Ontario L7N 2R8. Our phone number is 905-418-2735. We are located on the 3rd floor of the Marden Family Health Centre.
Nice to have
• We only need to have a logo, our address, a ballot of some sort on the door hanger and the details about the contest, the rest is up to you. We are moving towards the slogan "what makes you smile" at some point so this can be incorporated if it works with the overall design.
Should not have
• Fluorescent colours

```html
<!DOCTYPE html>
<html lang="en">
<head>
<meta charset="utf-8">
<title>Brightview Dental Group – Door Hanger</title>
<link href="https://fonts.googleapis.com/css2?family=Oswald:wght@500;600&family=Open+Sans:wght@400;600&display=swap" rel="stylesheet">
<style>
  :root {
    --stage: #575757;
    --ink: #000000;
    --night: #1e2129;
    --brand-blue: #3398f8;
    --paper: #ffffff;
    --rim: #3a3a3a;
    --map-fill: #efecee;
    --form-fill: #e3e3e3;
    --text: #1c1c1c;
  }
  * { box-sizing: border-box; margin: 0; padding: 0; }
  html, body { width: 1200px; height: 1200px; overflow: hidden; }
  body { background: var(--stage); position: relative; font-family: "Open Sans", sans-serif; }

  .hanger {
    position: absolute; top: 91px; width: 450px; height: 979px;
    box-shadow: 0 10px 14px rgba(0,0,0,.35);
    overflow: hidden;
  }
  .hanger--front { left: 79px; background: var(--night); }
  .hanger--back { left: 607px; background: var(--paper); }
  .hanger__shapes { position: absolute; inset: 0; }

  .photo-zone { position: absolute; left: 0; top: 330px; width: 450px; height: 430px; }

  .brand-name {
    position: absolute; left: 0; width: 450px; top: 250px;
    text-align: center; color: var(--paper);
    font-family: "Oswald", sans-serif; font-weight: 500;
    font-size: 40px; line-height: 42px; letter-spacing: 1px; text-transform: uppercase;
  }

  .slogan, .prize-band, .prize {
    position: absolute; left: 0; width: 450px; text-align: center;
    font-family: "Oswald", sans-serif; font-weight: 600; text-transform: uppercase;
    color: var(--paper);
  }
  .slogan { top: 770px; font-size: 36px; line-height: 54px; letter-spacing: -0.5px; }
  .prize-band { top: 829px; height: 48px; background: var(--brand-blue); font-size: 34px; line-height: 48px; }
  .prize { top: 892px; font-size: 36px; line-height: 56px; letter-spacing: -0.5px; }
  .prize__amount { font-size: 50px; }

  .headline {
    position: absolute; left: 0; width: 450px; top: 272px;
    text-align: center; color: var(--brand-blue);
    font-family: "Oswald", sans-serif; font-weight: 500;
    font-size: 40px; line-height: 53px; letter-spacing: -0.8px;
  }
  .location-map {
    position: absolute; left: 82px; top: 382px; width: 280px; height: 255px;
    background: var(--map-fill); border: 1px solid #555;
  }
  .contest-rules {
    position: absolute; left: 22px; width: 406px; top: 650px;
    text-align: center; color: var(--text); font-size: 13px; line-height: 17.6px;
  }
  .ballot {
    position: absolute; left: 40px; top: 733px; width: 373px; height: 220px;
    background: var(--form-fill); padding: 7px 30px 0 8px;
  }
  .ballot__row {
    display: flex; align-items: flex-end; height: 45.5px; gap: 8px;
    font-size: 14px; color: var(--text); font-weight: 500;
  }
  .ballot__row:first-child { height: 24px; }
  .ballot__line { flex: 1; border-bottom: 1.5px dashed #333; margin-bottom: 3px; }
</style>
</head>
<body>

<section class="hanger hanger--front" aria-label="Door hanger front">
  <svg class="hanger__shapes" width="450" height="979" viewBox="0 0 450 979">
    <rect width="450" height="979" fill="var(--night)"/>
    <rect width="450" height="360" fill="var(--ink)"/>
    <path d="M0 165 Q225 218 450 165 V337 Q225 372 0 337 Z" fill="var(--brand-blue)"/>
    <circle cx="225" cy="104" r="66" fill="var(--paper)"/>
  </svg>
  <div class="photo-zone" role="img" aria-label="Photo of a smiling woman with long blonde hair"
       style="clip-path: path('M0 7 Q225 32 450 7 V403 Q225 450 0 403 Z'); background: radial-gradient(ellipse at 55% 50%, #e3b797 0%, #c9a07d 28%, #dfe6ea 62%, #f3f6f8 100%);"></div>
  <div class="brand-name">Brightview<br>Dental Group</div>
  <div class="slogan">What Makes You Smile</div>
  <div class="prize-band">Enter To Win</div>
  <div class="prize"><span class="prize__amount">$1000</span> Travel Gift Card</div>
</section>

<section class="hanger hanger--back" aria-label="Door hanger back">
  <svg class="hanger__shapes" width="450" height="979" viewBox="0 0 450 979">
    <path d="M0 0 H450 V215 Q225 268 0 215 Z" fill="var(--rim)"/>
    <path d="M0 0 H450 V203 Q225 255 0 203 Z" fill="var(--ink)"/>
    <circle cx="225" cy="133" r="66" fill="var(--paper)"/>
  </svg>
  <h1 class="headline">Stop By Meet The Team<br>Enter To Win!</h1>
  <div class="location-map" role="img" aria-label="Street map showing the clinic location near Pinecrest Road"></div>
  <p class="contest-rules">The individual must come in person to drop off the ballot and during that time they will get a tour of the practice and meet key people. We are located on the 3rd floor of the Marden Family Health Centre.</p>
  <form class="ballot" aria-label="Contest ballot">
    <div class="ballot__row"><span>Name</span><span class="ballot__line"></span></div>
    <div class="ballot__row"><span>Address</span><span class="ballot__line"></span></div>
    <div class="ballot__row"><span>City</span><span class="ballot__line"></span></div>
    <div class="ballot__row"><span>Postal Code</span><span class="ballot__line"></span></div>
    <div class="ballot__row"><span>Email Address</span><span class="ballot__line"></span></div>
  </form>
</section>

</body>
</html>
```